re-skin an existing app using new logo and color scheme

The company that created the existing app TotGuard will be re-skinning the app on our behalf. We need to get a design submitted to them that retains the same functionality of their app but using our brand's look and feel. The product this app will be used in conjunction with is called Pulse Band.
Pulse Band is a stand-alone cellular watch that allows anyone from kids to seniors to make phone calls by simply pushing one of four buttons on the watch. The SOS button connects you to a live team of emergency professionals that can patch you to a 911 operator. Two of the other buttons are programmable to dial any desired phone number. The fourth button (called the "Magic" button) connects you with a live team of personal assistants that can help you with anything you want, including transferring you to any number, making dinner reservations, answering trivia, finding movie times and anything else you can imagine.
The built-in GPS functionality of the watch allows you to track the location of the watch at any time from the Pulse Band website or the Pulse Band app. You can also set up a perimeter around a specific area so that you can receive alerts when the watch travels outside of the "geofence".
Our slogan is: "Always safe on our watch"
We have included in the materials the Pulse Band logo (in Adobe Illustrator). We have also included screen shots of some of the screens of the existing app (TotGuard).
Using our logo, please design a re-skin of the attached screen shots. We want a simple, clean design. A great example of this is the Roam-n-Pin app:
https://www.folioshelf.net/gallery/Roam-n-Pin/5927143
For the login redesign, this can be redone as far as the placement of the fields and buttons etc. Please make sure to include the slogan "Always safe on our watch" somewhere on the login screen.
For the navigation screen, only the top part will be available for you to redesign - the bottom 80% of the screen needs to stay the same. (where it says "Device name: Teal Band" and below)
For the privilege screen, this can be completely redesigned.
For the family numbers setting screen, this can be completely redesigned.
For the whitelist setting screen, this can be completely redesigned.
Any questions, let us know.

```html
<!DOCTYPE html>
<html lang="en">
<head>
<meta charset="utf-8">
<title>Family Numbers Setting</title>
<link rel="stylesheet" href="https://fonts.googleapis.com/css2?family=Montserrat:wght@500;600&family=Questrial&display=swap">
<style>
  :root {
    --brand: #5fd3ee;
    --canvas: #f3f3f3;
    --ink: #4a4a4a;
    --field: #dddddd;
    --field-border: #555555;
    --divider: #bdbdbd;
    --white: #ffffff;
  }
  * { box-sizing: border-box; margin: 0; padding: 0; }
  html, body { width: 806px; height: 1200px; overflow: hidden; }
  body { background: var(--canvas); font-family: "Montserrat", sans-serif; position: relative; }

  .app-header { position: absolute; left: 0; top: 0; width: 806px; height: 184px; background: var(--brand); color: var(--white); }
  .status-bar { position: absolute; left: 0; top: 0; width: 100%; height: 76px; font-family: "Questrial", sans-serif; font-size: 25px; }
  .status-bar .signal { position: absolute; left: 28px; top: 28px; }
  .status-bar .carrier { position: absolute; left: 183px; top: 22px; }
  .status-bar .wifi { position: absolute; left: 278px; top: 20px; }
  .status-bar .clock { position: absolute; left: 365px; top: 22px; }
  .status-bar .indicators { position: absolute; left: 508px; top: 20px; }
  .status-bar .battery-level { position: absolute; left: 640px; top: 23px; }
  .status-bar .battery { position: absolute; left: 720px; top: 26px; }

  .screen-title { position: absolute; left: 100px; top: 96px; font-weight: 600; font-size: 36px; letter-spacing: 0.5px; line-height: 1; }
  .back-arrow { position: absolute; left: 36px; top: 100px; }

  .btn { position: absolute; background: var(--brand); color: var(--white); border: none; border-radius: 16px; font-family: "Montserrat", sans-serif; font-weight: 600; display: flex; align-items: center; justify-content: center; }
  .btn-get { left: 99px; top: 229px; width: 370px; height: 72px; font-size: 25px; }
  .btn-submit { left: 100px; top: 736px; width: 286px; height: 82px; font-size: 27px; }

  .number-row { position: absolute; left: 0; width: 806px; }
  .number-icon { position: absolute; left: 96px; }
  .number-field { position: absolute; left: 201px; width: 365px; height: 59px; background: var(--field); border: 3px solid var(--field-border); border-radius: 10px; font-family: "Questrial", sans-serif; font-size: 38px; color: var(--ink); padding-left: 18px; line-height: 53px; letter-spacing: -0.5px; }
  .divider { position: absolute; left: 98px; width: 537px; height: 2px; background: var(--divider); }
</style>
</head>
<body>
  <header class="app-header">
    <div class="status-bar">
      <svg class="signal" width="142" height="22" viewBox="0 0 142 22">
        <g fill="#fff" stroke="#fff" stroke-width="2">
          <circle cx="11" cy="11" r="9.5"/><circle cx="40" cy="11" r="9.5"/><circle cx="69" cy="11" r="9.5"/>
        </g>
        <g fill="none" stroke="#fff" stroke-width="2">
          <circle cx="98" cy="11" r="9.5"/><circle cx="127" cy="11" r="9.5"/>
        </g>
      </svg>
      <span class="carrier">Veralink</span>
      <svg class="wifi" width="40" height="28" viewBox="0 0 40 28">
        <g fill="none" stroke="#fff" stroke-width="4" stroke-linecap="round">
          <path d="M4 10 A23 23 0 0 1 36 10"/><path d="M10 16 A14 14 0 0 1 30 16"/>
        </g>
        <circle cx="20" cy="23" r="4" fill="#fff"/>
      </svg>
      <span class="clock">2:42 PM</span>
      <svg class="indicators" width="90" height="30" viewBox="0 0 90 30">
        <path d="M24 2 L2 12 L13 14 L15 25 Z" fill="#fff"/>
        <circle cx="52" cy="15" r="11" fill="#fff"/>
        <path d="M52 8 V15 H57" stroke="var(--brand)" stroke-width="2.5" fill="none"/>
        <path d="M78 6 L87 14 L81 19 V3 L87 8 L78 17" stroke="#fff" stroke-width="2" fill="none"/>
      </svg>
      <span class="battery-level">100%</span>
      <svg class="battery" width="66" height="24" viewBox="0 0 66 24">
        <rect x="1.5" y="2" width="40" height="18" rx="3" fill="none" stroke="#fff" stroke-width="2.5"/>
        <rect x="4" y="4.5" width="35" height="13" fill="#fff"/>
        <rect x="43" y="7" width="3" height="8" fill="#fff"/>
        <path d="M60 1 L53 13 H58 L55 23 L63 10 H58 Z" fill="#fff"/>
      </svg>
    </div>
    <svg class="back-arrow" width="28" height="42" viewBox="0 0 28 42">
      <path d="M27 1 L1 21 L27 41 Z" fill="#fff"/>
    </svg>
    <h1 class="screen-title">FAMILY NUMBERS SETTING</h1>
  </header>

  <main>
    <button class="btn btn-get">GET FAMILY NUMBER</button>

    <svg width="0" height="0" style="position:absolute">
      <defs>
        <g id="handset">
          <path d="M-20 14 C-24 4 -18 -6 -8 -14 C2 -21 12 -22 18 -18 L20 -14 L12 -5 L5 -9 C0 -7 -6 -2 -9 4 L-5 10 L-14 18 Z" fill="#fff"/>
        </g>
      </defs>
    </svg>

    <div class="number-row" style="top:350px">
      <svg class="number-icon" width="86" height="76" viewBox="0 0 86 76">
        <circle cx="38" cy="40" r="34" fill="var(--ink)"/>
        <use href="#handset" x="36" y="42"/>
        <circle cx="64" cy="18" r="17" fill="var(--ink)" stroke="var(--canvas)" stroke-width="2"/>
        <text x="64" y="27" text-anchor="middle" font-family="Montserrat, sans-serif" font-weight="600" font-size="25" fill="#fff">1</text>
      </svg>
      <div class="number-field" style="top:10px">1-372-555-148</div>
    </div>
    <div class="divider" style="top:455px"></div>

    <div class="number-row" style="top:481px">
      <svg class="number-icon" width="86" height="76" viewBox="0 0 86 76">
        <circle cx="38" cy="40" r="34" fill="var(--ink)"/>
        <use href="#handset" x="36" y="42"/>
        <circle cx="64" cy="18" r="17" fill="var(--ink)" stroke="var(--canvas)" stroke-width="2"/>
        <text x="64" y="27" text-anchor="middle" font-family="Montserrat, sans-serif" font-weight="600" font-size="25" fill="#fff">2</text>
      </svg>
      <div class="number-field" style="top:10px">1-418-555-176</div>
    </div>
    <div class="divider" style="top:587px"></div>

    <div class="number-row" style="top:613px">
      <svg class="number-icon" width="86" height="76" viewBox="0 0 86 76">
        <circle cx="38" cy="40" r="34" fill="var(--ink)"/>
        <use href="#handset" x="36" y="42"/>
        <circle cx="64" cy="18" r="17" fill="var(--ink)" stroke="var(--canvas)" stroke-width="2"/>
        <text x="64" y="27" text-anchor="middle" font-family="Montserrat, sans-serif" font-weight="600" font-size="25" fill="#fff">3</text>
      </svg>
      <div class="number-field" style="top:10px">1-529-555-264</div>
    </div>

    <button class="btn btn-submit">SUBMIT</button>
  </main>
</body>
</html>
```